E-commerce comic book retailer needs banner design for trade shows

Online retail business specializing in comic books and pop culture collectibles needs a banner design for trade show displays that promotes our mission to support charity through the sale of our merchandise. Our slogan is "Tall Folks Lifting Small Folks" and we donate 10% of our sales to the Youngsters' Hope Alliance / RiverGlen Health Children's Hospital. Banner will be part of a banquet table display draped with a medium blue table cloth.

Target Market(s)

Comic book and pop culture shoppers ages 10 to 80

Industry/Entity Type

Business

Font styles to use
Serif
Sans Serif

Requirements
Must have
• Final design must be vector art, with design sized print ready at 2.5 feet by 4 feet (76.2cm x 121.9cm) in landscape format. Elements to include...
• 1) Velmor Comics Logo (AI file attached)
• 2) Our slogan "Tall Folks Lifting Small Folks"
• 3) Youngsters' Hope Alliance and RiverGlen Health logos (attached, file provided by them with permission of use)
• 4) The following statement must be placed nearby the hospital logos “10% of sales benefits the Youngsters’ Hope Alliance & RiverGlen Health Children’s Hospital”
• 5) Our website, email and phone number - www.velmorcomics-example.com, info@velmorcomics-example.com, 1(555) 38 PANEL
• 6) Accepted payment methods area including logos for the following - Quindo Pay, Teskar Pay, Contactless Payment, EMV chip cards, MonWisp, Zelto Card, Orvane Card, Brightlo Card, Northvale Remit
• elements 2,3 and 4 should be grouped together as a main focal point of the banner
Nice to have
• fun, upbeat colors and/or patterns (we attached an old business card for possible inspiration)
Should not have
• fonts difficult to read quickly or busy/distracting colors or patterns

```html
<!DOCTYPE html>
<html lang="en">
<head>
<meta charset="utf-8">
<title>Velmor Comics – Trade Show Banner</title>
<link rel="stylesheet" href="https://fonts.googleapis.com/css2?family=Luckiest+Guy&family=Anton&family=Oswald:wght@500;700&family=Roboto:wght@700&display=swap">
<style>
  :root {
    --page: #ffffff;
    --banner-yellow: #fcc72e;
    --ink: #000000;
    --brand-red: #e3201b;
    --brand-blue: #1a8fe0;
    --slogan-grey: #b9b9b9;
    --slogan-edge: #555555;
    --art-light: #f1f1f1;
    --art-dark: #bcbcbc;
    --white: #ffffff;
    --pay-blue: #1a3a8f;
  }
  * { margin: 0; padding: 0; box-sizing: border-box; }
  html, body {
    width: 1200px; height: 846px; overflow: hidden;
    background: var(--page);
  }
  .canvas { position: relative; width: 1200px; height: 846px; }
  .banner {
    position: absolute; left: 120px; top: 123px;
    width: 960px; height: 600px;
    background: var(--banner-yellow);
    overflow: hidden;
  }
  .bubble { position: absolute; left: 0; top: 0; width: 960px; height: 600px; }

  .brand {
    position: absolute; left: 40px; top: 215px; width: 260px;
    text-align: center;
    font-family: "Luckiest Guy", "Anton", sans-serif;
    line-height: 0.95;
    white-space: nowrap;
  }
  .brand-name { font-size: 56px; color: var(--brand-red); }
  .brand-sub { font-size: 25px; color: var(--ink); margin-top: 8px; }
  .brand-phone { font-size: 27px; color: var(--brand-red); margin-top: 4px; }

  .donation {
    position: absolute; left: 50px; top: 425px;
    font-family: "Anton", sans-serif;
    white-space: nowrap;
  }
  .donation-big { font-size: 74px; line-height: 1; color: var(--brand-red); }
  .donation-line {
    font-family: "Oswald", sans-serif; font-weight: 700;
    font-size: 24px; color: var(--brand-blue); line-height: 1;
    margin-top: -4px;
  }
  .partners {
    position: absolute; left: 50px; top: 528px;
    width: 255px; height: 72px;
    background: var(--white);
    display: flex; align-items: center; gap: 10px; padding: 0 10px;
    font-family: "Roboto", sans-serif; font-size: 10px; line-height: 1.15;
  }
  .partner { display: flex; align-items: center; gap: 5px; }
  .partner-dot { width: 14px; height: 14px; border-radius: 50%; background: var(--banner-yellow); flex: none; }
  .partner-square { width: 14px; height: 14px; background: var(--pay-blue); flex: none; }
  .partner-hope { color: var(--brand-red); width: 95px; }
  .partner-river { color: var(--pay-blue); width: 110px; }

  .slogan {
    position: absolute; left: 410px; top: 22px;
    font-family: "Luckiest Guy", "Anton", sans-serif;
    font-size: 36px; line-height: 1.1;
    color: var(--slogan-grey);
    -webkit-text-stroke: 1.2px var(--slogan-edge);
    white-space: nowrap;
  }
  .story-art {
    position: absolute; left: 665px; top: 25px; width: 215px; height: 270px;
    background: linear-gradient(180deg, var(--art-light), var(--art-dark));
    border-radius: 30px;
  }

  .payments { position: absolute; left: 332px; top: 446px; width: 620px; }
  .payments-title {
    font-family: "Oswald", sans-serif; font-weight: 700;
    font-size: 22px; color: var(--ink);
    white-space: nowrap;
  }
  .payment-list {
    display: flex; align-items: center; gap: 10px; margin-top: 16px;
    font-family: "Oswald", sans-serif; font-weight: 500;
    font-size: 12px; color: var(--pay-blue); list-style: none;
  }
  .payment-list li { display: flex; align-items: center; gap: 4px; white-space: nowrap; }
  .payment-dot { width: 9px; height: 9px; border-radius: 50%; background: var(--pay-blue); }

  .contact-band {
    position: absolute; left: 320px; top: 545px; width: 660px; height: 55px;
    background: var(--ink); border-radius: 28px 0 0 28px;
    font-family: "Luckiest Guy", "Anton", sans-serif; font-size: 17px;
    color: var(--banner-yellow);
    display: flex; align-items: center; padding-left: 22px;
    white-space: nowrap; overflow: hidden;
  }
</style>
</head>
<body>
<div class="canvas">
  <section class="banner">
    <svg class="bubble" viewBox="0 0 960 600" aria-hidden="true">
      <path d="M315 -10 Q330 110 420 125 Q395 215 470 250 Q470 320 560 325 Q600 400 690 380 Q760 420 820 375 L845 472 L840 362 Q930 360 925 285 Q985 255 975 180 L975 -10 Z"
            fill="var(--white)" stroke="var(--ink)" stroke-width="9" stroke-linejoin="round"/>
    </svg>

    <div class="slogan">Tall Folks<br>Lifting<br>Small Folks</div>
    <div class="story-art" role="img" aria-label="Illustration of a man in an armchair reading a book to a group of children"></div>

    <div class="brand">
      <div class="brand-name">Velmor<br>Comics</div>
      <div class="brand-sub">&amp; Collectibles</div>
      <div class="brand-phone">1(555) 38 PANEL</div>
    </div>

    <div class="donation">
      <div class="donation-big">10% of</div>
      <div class="donation-line">OUR SALES TO THE</div>
    </div>
    <div class="partners">
      <div class="partner partner-hope"><span class="partner-dot"></span>Youngsters' Hope Alliance</div>
      <div class="partner partner-river"><span class="partner-square"></span>RiverGlen Health Children's Hospital</div>
    </div>

    <div class="payments">
      <div class="payments-title">SECURE PAYMENTS BY:-</div>
      <ul class="payment-list">
        <li>MonWisp</li>
        <li>Orvane Card</li>
        <li>Zelto Card</li>
        <li>Northvale Remit</li>
        <li>Brightlo Card</li>
        <li>Quindo Pay</li>
        <li><span class="payment-dot"></span>Contactless</li>
        <li>Teskar Pay</li>
      </ul>
    </div>

    <div class="contact-band">www.velmorcomics-example.com, info@velmorcomics-example.com</div>
  </section>
</div>
</body>
</html>
```